Smart, Classy, Conservative looking Legal Letterhead

I need a letterhead that when you look at it it "says to you " this is a well established law firm with very smart lawyers, which will one day be appearing before the Supreme Court of the USA. All information about the Law firm should appear at the top of the page. please no information in the footer.

Industry/Entity Type

Legal

Requirements
Must have
• The name of the law firm, both addresses, phone number and fax,, The names of the attorneys, the website.
• Fields that get changed such as the date, VIA, Address of who the letter is going to,
• Re, Index,
• should have a clean neat look, sleek
Nice to have
• some color would be nice. A logo of some sort could be nice as well. Maybe a single S or interlocking B's For Brevik and Brevik.
Should not have
• not too modern looking.

```html
<!DOCTYPE html>
<html lang="en">
<head>
<meta charset="utf-8">
<title>Brevik &amp; Brevik, LLP — Letterhead</title>
<link rel="stylesheet" href="https://fonts.googleapis.com/css2?family=Oswald:wght@300&family=Tinos&display=swap">
<style>
  :root {
    --ink: #2b2b2b;
    --text: #3a3a3a;
    --muted: #555555;
    --rule: #3c3c3c;
    --paper: #ffffff;
  }
  html, body {
    margin: 0;
    padding: 0;
    overflow: hidden;
    background: var(--paper);
  }
  .page {
    position: relative;
    width: 836px;
    height: 1200px;
    background: var(--paper);
    color: var(--text);
    font-family: "Tinos", "Times New Roman", serif;
    overflow: hidden;
  }
  .firm-mark {
    position: absolute;
    left: 384px;
    top: 44px;
    width: 78px;
    height: 78px;
  }
  .firm-name {
    position: absolute;
    left: 0;
    right: 0;
    top: 131px;
    margin: 0;
    text-align: center;
    font-family: "Oswald", "Arial Narrow", sans-serif;
    font-weight: 300;
    font-size: 35px;
    letter-spacing: 0.6px;
    color: var(--ink);
    line-height: 1.1;
  }
  .office {
    position: absolute;
    top: 52px;
    margin: 0;
    font-style: normal;
    font-size: 11.5px;
    line-height: 15px;
    color: var(--muted);
  }
  .office-label {
    font-size: 10px;
    letter-spacing: 1.5px;
    text-transform: uppercase;
    color: var(--ink);
  }
  .office-main { left: 42px; }
  .office-branch { right: 48px; text-align: right; }
  .head-rule {
    position: absolute;
    left: 40px;
    top: 189px;
    width: 748px;
    height: 3px;
    background: var(--rule);
  }
  .firm-contacts {
    position: absolute;
    left: 40px;
    top: 197px;
    width: 748px;
    margin: 0;
    text-align: center;
    font-size: 11px;
    line-height: 14px;
    color: var(--muted);
    letter-spacing: 0.3px;
  }
  .recipient {
    position: absolute;
    left: 57px;
    top: 228px;
    margin: 0;
    font-style: normal;
    font-size: 16.4px;
    line-height: 17.3px;
  }
  .recipient .ref {
    font-size: 13px;
    line-height: 15.5px;
  }
  .recipient .ref-value {
    text-decoration: underline;
  }
  .letter-fields {
    position: absolute;
    right: 48px;
    top: 228px;
    margin: 0;
    text-align: right;
    font-size: 15px;
    line-height: 19px;
  }
  .salutation {
    position: absolute;
    left: 53px;
    top: 535px;
    margin: 0;
    font-size: 21.4px;
  }
  .body-text {
    position: absolute;
    left: 55px;
    top: 574px;
    width: 712px;
    margin: 0;
    font-size: 19.8px;
    line-height: 23px;
    text-indent: 30px;
  }
  .closing {
    position: absolute;
    left: 478px;
    top: 632px;
    margin: 0;
    font-size: 21.2px;
  }
  .signatory {
    position: absolute;
    left: 571px;
    top: 710px;
    margin: 0;
    font-size: 21.3px;
  }
</style>
</head>
<body>
  <main class="page">
    <header class="letterhead">
      <address class="office office-main">
        <span class="office-label">Main Office</span><br>
        1180 Veterans Parkway, Suite 310<br>
        Lakemont, NY 11790
      </address>
      <svg class="firm-mark" viewBox="0 0 78 78" aria-hidden="true">
        <circle cx="39" cy="39" r="37.5" fill="none" stroke="var(--ink)" stroke-width="1.6"/>
      </svg>
      <address class="office office-branch">
        <span class="office-label">Manhattan Office</span><br>
        415 Crestline Avenue, 12th Floor<br>
        New York, NY 10017
      </address>
      <h1 class="firm-name">BREVIK &amp; BREVIK, LLP</h1>
      <div class="head-rule"></div>
      <p class="firm-contacts">Daniel A. Brevik &middot; Margaret L. Brevik &nbsp;|&nbsp; Tel (631) 555-0148 &middot; Fax (631) 555-0149 &nbsp;|&nbsp; www.brevikbrevik-law.com</p>
    </header>

    <address class="recipient">
      Hon. Fake Judge Name Here<br>
      United States District Court, E.D.N.Y.<br>
      240 Harbor Plaza<br>
      Courtroom XXXXX<br>
      Lakemont, NY 11790-4021<br>
      <span class="ref">Re:<span class="ref-value">XXXXXXXXXXXXXXXXXXX</span></span><br>
      <span class="ref">Index:XXXXXXXX</span>
    </address>

    <p class="letter-fields">
      Date: XXXXXXXX<br>
      VIA: XXXXXXXX
    </p>

    <p class="salutation">Your Honor:</p>
    <p class="body-text">Pursuant to Your Honor's Individual Practices Rule III(C)(3), enclosed please find a courtesy copy of Plaintiff's Revised Yadda Yadda Yadda.</p>
    <p class="closing">Respectfully,</p>
    <p class="signatory">Daniel A. Brevik</p>
  </main>
</body>
</html>
```